Hospital Website Design - PSD only

We need a web design for a community hospital based in Uniontown, Pennsylvania.

We would like to see a first round of designs for the website HOMEPAGE. Once we have selected finalists for the look & feel, based on the submitted homepage designs, we will request an additional INTERNAL page design.

Both designs should follow the content requirements displayed on the attached wireframes. I will post the internal page wireframe after the homepage design finalists are selected.

The desired Look & Feel for the website is clean and modern.

3 sites we like are:
http://www.marvellcare.org/
http://www.qrtm.org/
http://www.dellwyn.org/

Attached are the Homepage wireframe, and the Brackfield Hospital Logo.

The winning design will communicate a bright, healthy, energetic, community-oriented feeling.

Please note that readability is very important for a hospital website. Font-sizes and line-heights should be carefully selected for comfortable reading.
Updates

Dear designers -- Please don't feel locked into the exact shades of blue / brown used in the logo. We find this color scheme quite ugly and are working on a logo update. The new color scheme will probably still involve some shades of blue and brown, but we aren't sure yet. Please use your best judgement to make a beautiful design, similar in style to the modern / simple aesthetic of http://www.marvellcare.org/ We will be working on feedback to designs today. Thank you.

Regarding Large Rotating Graphic area and Navigation: We prefer a full-width display, rather than boxed. The navigation should be visually prominent, easy to read text that one can scan easily across the top of the page. Again, please refer to http://www.marvellcare.org/ for our preferred design aesthetic. Some of the designs submitted have been somewhat dated in their styling. We'd like a polished, modern, crisp, bold, beautiful design.

Re: choice of image in large rotating graphic area -- Designers, please do not use stock photography of a group of doctors, or a nursing home scene, in your sample rotating graphic areas. Although this should not affect our perception of the design, it throws off everything in the page if we don't like the image. Please try to select a bold / attractive image that you would like to set the tone for your design.

Reason: Extending our deadline to receive more designs exploring other color options containing less brown, or browns with a more attractive vibe. We would also like to see designs that are not exact replicas of the wireframe. The wireframe is just to show the elements on the page. Please use your creativity to utilize these elements in an attractive layout that we will like. We would also prefer to see use of photography that shows a younger, more cheerful, hopeful feeling in the design... and where the photographs are consistent with your design approach. Thanks!

In general, feedback for everyone is, please look here: http://www.marvellcare.org/ that's the feeling / vibe we want. DO NOT let the old, ugly, outdated logo determine your design. We are having the logo redesigned. DO NOT take an ugly, outdated template, and adapt it for this website. We want to see something BEAUTIFUL!!! Please give us your best effort! People who come to this website are in health crisis, and they want to be uplifted!! Their good spirits are in your hands.

Reason: We are still reviewing submissions and working with designers to provide better feedback. Thanks for your patience.

Reason: our sincerest apologies for the failure to provide adequate feedback this week. We hit a snag with the various decision makers on this project and were not able to review the recent submissions. We will make every effort to have a decision by tomorrow. Thank you for your patience.

Target Market(s)

Adults based in suburban & rural community, aged 18-80.

Industry/Entity Type

Hospital

Requirements
Must have
• The design must include all of the content areas outlined on the attached wireframe.
The design must include the attached logo. (Note, we may update the logo during the design contest, but it will not be changed dramatically. It will just be modernized slightly.)
Nice to have
• Show hover states for things like Navigation, Links, or small images in gallery, so we can see how you imagine interactive states.

```html
<!DOCTYPE html>
<html lang="en">
<head>
<meta charset="utf-8">
<title>Brackfield Hospital – Home</title>
<link href="https://fonts.googleapis.com/css2?family=Barlow:wght@400;500;600;700&family=Barlow+Semi+Condensed:wght@500;600;700&display=swap" rel="stylesheet">
<style>
:root{
  --brown:#9c7b55;
  --nav-brown:#9a7450;
  --ink:#1b3c72;
  --line:#d9d9d9;
  --white:#ffffff;
}
*{box-sizing:border-box;margin:0;padding:0}
html,body{width:930px;height:1200px;overflow:hidden;background:var(--white)}
body{font-family:"Barlow",sans-serif;color:var(--ink);position:relative}
.abs{position:absolute}

/* header */
.contact{left:46px;top:10px;font-size:11.5px;color:var(--ink);letter-spacing:.2px}
.brand{left:46px;top:38px;display:flex;align-items:center;gap:8px}
.brand-mark{width:14px;height:14px;border-radius:50%;background:var(--brown)}
.brand-name{font-size:17px;font-weight:500;color:var(--ink);letter-spacing:.3px}
.brand-tag{left:68px;top:62px;font-size:7px;color:var(--ink)}
.lang{top:20px;width:50px;text-align:center;font-size:7.5px;color:var(--ink)}
.lang svg{display:block;margin:0 auto 3px}
.site-search{left:678px;top:52px;width:211px;height:22px;background:#e6e8eb;border:1px solid #cfd3d8;display:flex;align-items:center;padding:0 10px;gap:8px;font-size:8px;color:var(--ink)}
.site-search .clear{margin-left:auto;width:13px;height:13px;border-radius:50%;background:#fff}
.main-nav{left:0;top:104px;width:930px;text-align:center;font-family:"Barlow Semi Condensed",sans-serif;font-weight:700;font-size:15px;color:var(--nav-brown);letter-spacing:.35px;white-space:nowrap}
.main-nav span{margin:0 3px}
.header-rule{left:0;top:130px;width:930px;height:1px;background:#e2e2e2}

/* hero */
.hero{left:0;top:131px;width:930px;height:274px;overflow:hidden;
  background:
    radial-gradient(ellipse 110px 150px at 120px 260px,rgba(120,165,215,.95),rgba(120,165,215,0) 70%),
    radial-gradient(ellipse 90px 120px at 300px 280px,rgba(238,241,244,.95),rgba(238,241,244,0) 70%),
    radial-gradient(ellipse 80px 120px at 450px 290px,rgba(86,120,160,.85),rgba(86,120,160,0) 70%),
    radial-gradient(ellipse 120px 150px at 620px 270px,rgba(246,247,249,.98),rgba(246,247,249,0) 70%),
    radial-gradient(ellipse 110px 150px at 820px 270px,rgba(242,244,247,.95),rgba(242,244,247,0) 70%),
    radial-gradient(ellipse 260px 80px at 470px 40px,rgba(255,255,255,.75),rgba(255,255,255,0) 70%),
    linear-gradient(90deg,rgba(70,90,110,.35) 0%,rgba(70,90,110,0) 18%,rgba(70,90,110,0) 82%,rgba(70,90,110,.35) 100%),
    linear-gradient(180deg,#e3e5e7 0%,#cdd1d4 40%,#a9afb5 100%)}
.hero-caption{left:189px;top:313px;width:552px;height:75px;background:rgba(156,123,85,.88);padding:5px 0 0 24px;color:#fff}
.hero-caption h1{font-family:"Barlow Semi Condensed",sans-serif;font-size:31px;font-weight:700;letter-spacing:.5px;line-height:36px}
.hero-caption p{font-size:19px;font-weight:500;margin-top:3px}
.hero-arrow{top:323px;width:60px;height:60px;border-radius:50%;background:rgba(156,123,85,.85)}
.hero-arrow svg{position:absolute;left:24px;top:22px}

/* quick band */
.quick-band{left:0;top:405px;width:930px;height:87px;background:var(--brown)}
.condition-title{left:45px;top:424px;color:#fff;font-family:"Barlow Semi Condensed",sans-serif;font-weight:700;font-size:14.5px;letter-spacing:.3px}
.condition-search{left:48px;top:450px;width:211px;height:23px;background:#f3f3f3;display:flex;align-items:center;gap:8px;padding:0 10px;font-size:10px;color:var(--ink)}
.condition-search .clear{margin-left:auto;width:13px;height:13px;border-radius:50%;background:#ddd}
.quick-link{top:415px;height:70px;border-left:2px solid #fff;display:flex;align-items:center;justify-content:center;text-align:center;color:#fff;font-family:"Barlow Semi Condensed",sans-serif;font-weight:600;font-size:12.5px;line-height:16px}
.quick-end{left:877px;top:415px;height:70px;border-left:2px solid #fff}

/* middle */
.gallery{left:29px;top:512px;width:423px;height:219px;border:2px solid var(--line);background:#fafafa}
.thumb{width:65px;height:65px;border:1px solid #ccc}
.gallery-video{left:180px;top:518px;width:266px;height:206px;
  background:
    radial-gradient(ellipse 60px 90px at 50px 150px,rgba(60,52,48,.85),rgba(60,52,48,0) 70%),
    radial-gradient(ellipse 70px 60px at 150px 150px,rgba(70,130,185,.85),rgba(70,130,185,0) 70%),
    radial-gradient(ellipse 70px 80px at 230px 170px,rgba(40,45,55,.8),rgba(40,45,55,0) 70%),
    linear-gradient(90deg,#d9dee2 0%,#b9c2c9 50%,#cfd6db 100%)}
.play{left:270px;top:585px}
.box{border:2px solid var(--line);background:#fff}
.box-head{background:var(--brown);color:#fff;font-family:"Barlow Semi Condensed",sans-serif;font-weight:700;font-size:14.5px;padding:0 12px;height:40px;display:flex;align-items:center;letter-spacing:.3px}
.visit{left:479px;top:512px;width:196px;height:219px}
.visit ul{list-style:none;padding:8px 0 0 14px}
.visit li{font-size:11.5px;font-weight:600;line-height:19.4px;display:flex;align-items:center;gap:9px}
.visit li::before{content:"";width:5px;height:5px;border-radius:50%;background:var(--brown)}
.portal{left:702px;top:512px;width:197px;height:73px;background:var(--brown);border:2px solid var(--line);padding:4px 10px;color:#fff}
.portal-title{font-size:9.5px;font-weight:600}
.portal-field{width:122px;height:15px;background:#fff;color:var(--ink);font-size:11px;font-weight:600;padding-left:8px;line-height:15px;margin:4px 0 0 4px}
.portal-login{right:10px;top:42px;font-size:9px;font-weight:600}
.portal-new{left:12px;top:57px;font-size:8.5px;font-weight:600}
.resources{left:702px;top:593px;width:197px;height:138px}
.resources a{display:block;margin:0 6px 0 10px;padding:3px 0;font-size:11.5px;font-weight:600;color:var(--ink);text-decoration:none;border-bottom:1px solid #e4e4e4;line-height:13.5px}
.resources a:first-of-type{margin-top:10px}
.resources a:last-of-type{border-bottom:0}

/* news */
.tab{top:756px;height:28px;display:flex;align-items:center;justify-content:center;font-size:11.5px;font-weight:600}
.tab-news{left:55px;width:120px;border:2px solid var(--line);border-bottom:0;background:#fff;z-index:2;color:var(--ink)}
.tab-events{left:177px;width:160px;background:var(--brown);color:#fff;border:2px solid var(--line);border-bottom:0}
.news-panel{left:29px;top:782px;width:870px;height:278px;border:2px solid var(--line);background:#fff}
.story{top:798px;width:151px}
.story-img{width:151px;height:126px}
.story p{margin-top:12px;font-size:11.6px;line-height:15.6px;color:var(--ink);letter-spacing:.05px}
.view-all{left:0;top:1046px;width:930px;text-align:center;font-size:11.5px;font-weight:600;letter-spacing:.3px}

/* footer */
.site-footer{left:0;top:1096px;width:930px;height:104px;background:var(--brown)}
.footer-links{left:111px;top:1123px;font-family:"Barlow Semi Condensed",sans-serif;font-weight:700;font-size:15.2px;color:#fff;letter-spacing:.45px;white-space:nowrap}
.footer-awards{left:111px;top:1150px;font-family:"Barlow Semi Condensed",sans-serif;font-weight:700;font-size:18px;color:#fff}
.social{top:1151px;width:22px;height:22px;border-radius:50%;background:#fff}
</style>
</head>
<body>

<header>
  <div class="abs contact">(555) 014 - 2700 | CONTACT US</div>
  <div class="abs brand"><span class="brand-mark"></span><span class="brand-name">BRACKFIELD HOSPITAL</span></div>
  <div class="abs brand-tag">Caring for our neighbors every day</div>

  <div class="abs lang" style="left:779px">
    <svg width="22" height="15" role="img" aria-label="English flag"><rect width="22" height="15" fill="#b8324a"/><rect y="5" width="22" height="2" fill="#fff"/><rect y="10" width="22" height="2" fill="#fff"/><rect width="10" height="8" fill="#2c3f7a"/></svg>ENGLISH
  </div>
  <div class="abs lang" style="left:846px">
    <svg width="22" height="15" role="img" aria-label="Spanish flag"><rect width="22" height="15" fill="#c8202b"/><rect y="4" width="22" height="7" fill="#f3c320"/></svg>ESPANIOL
  </div>

  <div class="abs site-search">
    <svg width="10" height="10" viewBox="0 0 10 10"><circle cx="4" cy="4" r="3" fill="none" stroke="#1b3c72" stroke-width="1.4"/><line x1="6.2" y1="6.2" x2="9.3" y2="9.3" stroke="#1b3c72" stroke-width="1.4"/></svg>
    SEARCH<span class="clear"></span>
  </div>

  <nav class="abs main-nav">
    OUR SERVICES <span>|</span> FACILITIES &amp; DIRECTIONS <span>|</span> PATIENT &amp; VISITORS INFOMRATION <span>|</span> FIND A DOCTOR <span>|</span> HEALTH &amp; WELLNESS
  </nav>
  <div class="abs header-rule"></div>
</header>

<section>
  <div class="abs hero" role="img" aria-label="Photo of a smiling care team of doctors and nurses in white coats and scrubs in a bright clinic hallway"></div>
  <div class="abs hero-caption">
    <h1>CANCER CARE CENTER</h1>
    <p>The best doctors and nurses, and treatment close to home</p>
  </div>
  <div class="abs hero-arrow" style="left:785px"><svg width="12" height="16"><path d="M9 2 L3 8 L9 14" fill="none" stroke="#fff" stroke-width="2.5"/></svg></div>
  <div class="abs hero-arrow" style="left:855px"><svg width="12" height="16"><path d="M3 2 L9 8 L3 14" fill="none" stroke="#fff" stroke-width="2.5"/></svg></div>
</section>

<section>
  <div class="abs quick-band"></div>
  <div class="abs condition-title">DO YOU WANT TO LEARN ABOUT A CONDITION</div>
  <div class="abs condition-search">
    <svg width="10" height="10" viewBox="0 0 10 10"><circle cx="4" cy="4" r="3" fill="none" stroke="#1b3c72" stroke-width="1.4"/><line x1="6.2" y1="6.2" x2="9.3" y2="9.3" stroke="#1b3c72" stroke-width="1.4"/></svg>
    Diabetes, Cancer, heart health, ...<span class="clear"></span>
  </div>
  <div class="abs quick-link" style="left:381px;width:129px">SYMPTOMS<br>CHECKER</div>
  <div class="abs quick-link" style="left:510px;width:126px">SCHEDULE A<br>LAB TEST</div>
  <div class="abs quick-link" style="left:636px;width:121px">ONLINE BILL<br>PAY</div>
  <div class="abs quick-link" style="left:757px;width:120px">SUPPRT OUR<br>WORK</div>
  <div class="abs quick-end"></div>
</section>

<section>
  <div class="abs gallery"></div>
  <div class="abs thumb" style="left:37px;top:518px;background:radial-gradient(circle at 60% 70%,#3a5f9a 0,#3a5f9a 20%,transparent 55%),linear-gradient(135deg,#eef1f4,#b9c6d3)" role="img" aria-label="Doctor in a white coat and tie"></div>
  <div class="abs thumb" style="left:108px;top:518px;background:radial-gradient(circle at 50% 80%,#ffffff 0,#ffffff 25%,transparent 60%),linear-gradient(135deg,#f4efe9,#d3bea4)" role="img" aria-label="Physician with stethoscope"></div>
  <div class="abs thumb" style="left:37px;top:588px;background:radial-gradient(circle at 70% 60%,#f2f4f6 0,#f2f4f6 22%,transparent 55%),linear-gradient(135deg,#d5e3f1,#7f9ab7)" role="img" aria-label="Doctor consulting a patient"></div>
  <div class="abs thumb" style="left:108px;top:588px;background:radial-gradient(circle at 35% 65%,#f6f6f6 0,#f6f6f6 20%,transparent 50%),linear-gradient(135deg,#ecdcc6,#a9835d)" role="img" aria-label="Doctor with a young patient"></div>
  <div class="abs thumb" style="left:37px;top:658px;background:radial-gradient(circle at 40% 40%,#5fa3bd 0,#5fa3bd 22%,transparent 55%),linear-gradient(135deg,#9ccadb,#2c6a84)" role="img" aria-label="Surgical team in the operating room"></div>
  <div class="abs thumb" style="left:108px;top:658px;background:radial-gradient(circle at 65% 55%,#ffffff 0,#ffffff 22%,transparent 55%),linear-gradient(135deg,#efe6dc,#b99d83)" role="img" aria-label="Nurse checking a child"></div>
  <div class="abs gallery-video" role="img" aria-label="Video still of patients seated in a hospital waiting room"></div>
  <svg class="abs play" width="76" height="76" viewBox="0 0 76 76"><circle cx="38" cy="38" r="34" fill="rgba(255,255,255,.15)" stroke="#fff" stroke-width="4"/><path d="M30 22 L54 38 L30 54 Z" fill="#fff"/></svg>

  <div class="abs box visit">
    <div class="box-head">ABOUT YOUR VISIT</div>
    <ul>
      <li>Emergency Care</li>
      <li>Accepted Health Plans</li>
      <li>Pre-registration for Surgery</li>
      <li>Lab Hours</li>
      <li>Find a Phone Number</li>
      <li>Find a Form</li>
      <li>Pay Bill Online</li>
      <li>Visitor Guide</li>
    </ul>
  </div>

  <div class="abs portal">
    <div class="portal-title">Brackfield Patient Portal</div>
    <div class="portal-field">Password</div>
    <div class="portal-field">Email</div>
    <div class="abs portal-login">login ››</div>
    <div class="abs portal-new">new user? create account</div>
  </div>

  <div class="abs box resources">
    <div class="box-head">PATIENT RESOURCES</div>
    <a href="#">Tips on choosing the right doctor</a>
    <a href="#">Billing, Forms &amp; Medical Records</a>
    <a href="#">Making the best of the year</a>
    <a href="#">Appointment</a>
  </div>
</section>

<section>
  <div class="abs news-panel"></div>
  <div class="abs tab tab-news">BH News</div>
  <div class="abs tab tab-events">Upcoming Classes &amp; Events</div>

  <article class="abs story" style="left:55px"><div class="story-img" style="background:radial-gradient(ellipse 40px 60px at 115px 80px,#3f7fc0,transparent 70%),linear-gradient(90deg,#f6f7f8 0%,#e8edf2 50%,#b7c9dc 100%)" role="img" aria-label="Doctor with stethoscope in a clinic"></div><p>Lorem ipsum dolor sit amet, consectetuer adipiscing elit. Aenean commodo ligula eget dolor. Aenean massa. Cum sociis natoque penati-bus et magnis dis parturient montes, nascetur ridiculus</p></article>
  <article class="abs story" style="left:222px"><div class="story-img" style="background:linear-gradient(180deg,#5d86b3 0%,#9fbad6 35%,#f2f3f4 45%,#f2f3f4 70%,#9fbad6 80%,#dfe6ee 100%)" role="img" aria-label="Hospital building entrance sign"></div><p>Lorem ipsum dolor sit amet, consectetuer adipiscing elit. Aenean commodo ligula eget dolor. Aenean massa. Cum sociis natoque penati-bus et magnis dis parturient montes, nascetur ridiculus</p></article>
  <article class="abs story" style="left:390px"><div class="story-img" style="background:radial-gradient(ellipse 70px 30px at 60px 105px,#ffffff,transparent 70%),radial-gradient(ellipse 25px 50px at 115px 60px,#5b86a6,transparent 70%),linear-gradient(135deg,#eef0f1,#a4adb4)" role="img" aria-label="Doctor visiting a patient in bed"></div><p>Lorem ipsum dolor sit amet, consectetuer adipiscing elit. Aenean commodo ligula eget dolor. Aenean massa. Cum sociis natoque penati-bus et magnis dis parturient montes, nascetur ridiculus</p></article>
  <article class="abs story" style="left:557px"><div class="story-img" style="background:radial-gradient(ellipse 18px 50px at 85px 75px,#4a8fc4,transparent 70%),radial-gradient(ellipse 18px 50px at 115px 78px,#4a8fc4,transparent 70%),linear-gradient(90deg,#e6f1ef,#b5d8d2 60%,#7fb3a8)" role="img" aria-label="Staff walking down a bright hospital corridor"></div><p>Lorem ipsum dolor sit amet, consectetuer adipiscing elit. Aenean commodo ligula eget dolor. Aenean massa. Cum sociis natoque penati-bus et magnis dis parturient montes, nascetur ridiculus</p></article>
  <article class="abs story" style="left:725px"><div class="story-img" style="background:linear-gradient(180deg,#c3d3e3 0%,#d9e2ea 45%,#f6f6f6 62%,#ffffff 85%,#dfe3e6 100%)" role="img" aria-label="Medical staff group outside a hospital building"></div><p>Lorem ipsum dolor sit amet, consectetuer adipiscing elit. Aenean commodo ligula eget dolor. Aenean massa. Cum sociis natoque penati-bus et magnis dis parturient montes, nascetur ridiculus</p></article>

  <div class="abs view-all">VIEW ALL STORIES</div>
</section>

<footer>
  <div class="abs site-footer"></div>
  <div class="abs footer-links">REFERRING PHYSICIANS&nbsp; | &nbsp;MEDICAL PROFISSIONALS&nbsp; | &nbsp;GIVING&nbsp; | &nbsp;VOLUNTEERING&nbsp; | &nbsp;CAREERS&nbsp; | &nbsp;ONLINE BILL PAY</div>
  <div class="abs footer-awards">AWARDS</div>
  <div class="abs social" style="left:724px"></div>
  <div class="abs social" style="left:761px"></div>
  <div class="abs social" style="left:798px"></div>
</footer>

</body>
</html>
```